" Atendimento médico em consultório/Clinica para mulheres em geral. A clinica contará com três médicas ginecologistas. Inicialmente somente a Dra. Lívia atenderá. O principal valor da Clinica é com o cuidado com a Mulher através de atendimento individual e cuidadoso através de especialistas nas áreas da ginecologia e Obstetricia. Apesar de possuir atendimento Obstétrico, o mesmo não será o principal foco da clinica. "

```html
<!DOCTYPE html>
<html lang="pt-BR">
<head>
<meta charset="UTF-8">
<title>Assinatura de e-mail — Ginecologia Aurora</title>
<link href="https://fonts.googleapis.com/css2?family=Cormorant+Garamond:wght@400;500&family=Open+Sans:wght@400&display=swap" rel="stylesheet">
<style>
  :root {
    --bg: #e9e9eb;
    --card: #ffffff;
    --rose: #d9737b;
    --rose-soft: #f2c9cc;
    --rose-light: #fbe9ea;
    --grey-text: #8a8a8a;
    --dark-text: #5a5a5a;
    --figure-grey: #d6d6d8;
  }
  * { margin: 0; padding: 0; box-sizing: border-box; }
  html, body { width: 1200px; height: 1200px; overflow: hidden; }
  body {
    background: var(--bg);
    display: flex; align-items: center; justify-content: center;
    font-family: "Open Sans", sans-serif;
  }
  .signature {
    position: relative;
    width: 1120px; height: 280px;
    background: var(--card);
    border-radius: 14px;
    border-top: 4px solid var(--rose);
    border-bottom: 14px solid var(--rose);
    box-shadow: 0 4px 14px rgba(0,0,0,0.12);
    overflow: hidden;
  }
  .signature::after {
    content: ""; position: absolute; left: 0; right: 0; bottom: 10px;
    height: 3px; background: var(--rose-soft);
  }
  .brand {
    position: absolute; left: 40px; top: 36px; width: 320px;
    text-align: center;
  }
  .brand-mark {
    width: 86px; height: 86px; border-radius: 50%;
    background: var(--rose-light); border: 2px solid var(--rose-soft);
    margin: 0 auto 10px;
  }
  .brand-name {
    font-family: "Cormorant Garamond", serif; font-weight: 500;
    font-size: 40px; color: var(--rose); line-height: 1.05;
  }
  .brand-doctor {
    font-family: "Cormorant Garamond", serif; font-weight: 400;
    font-size: 25px; color: var(--grey-text); margin-top: 4px;
  }
  .divider {
    position: absolute; left: 388px; top: 40px;
    width: 3px; height: 170px; background: var(--rose);
  }
  .doctor {
    position: absolute; left: 414px; top: 98px;
  }
  .doctor-name {
    font-family: "Cormorant Garamond", serif; font-weight: 500;
    font-size: 32px; color: var(--rose); line-height: 1.1;
    white-space: nowrap;
  }
  .doctor-role { font-size: 16px; color: var(--grey-text); margin-top: 4px; }
  .contacts {
    position: absolute; left: 790px; top: 28px;
    list-style: none; font-size: 13px; color: var(--dark-text);
    line-height: 1.35;
  }
  .contacts li { display: flex; align-items: flex-start; gap: 10px; margin-bottom: 14px; }
  .contacts svg { flex: none; width: 22px; height: 22px; }
  .figure {
    position: absolute; right: 0; top: 0; width: 150px; height: 262px;
    background: linear-gradient(160deg, var(--figure-grey) 0%, var(--rose-soft) 55%, var(--rose) 100%);
    opacity: 0.85;
  }
</style>
</head>
<body>
  <div class="signature">
    <div class="brand">
      <div class="brand-mark"></div>
      <div class="brand-name">Ginecologia Aurora</div>
      <div class="brand-doctor">Dra. Lívia Moraes Tavares</div>
    </div>

    <div class="divider"></div>

    <div class="doctor">
      <div class="doctor-name">Dra. Lívia Moraes Tavares</div>
      <div class="doctor-role">Ginecologista CRM:0000</div>
    </div>

    <ul class="contacts">
      <li>
        <svg viewBox="0 0 22 22"><circle cx="11" cy="11" r="10" fill="var(--rose)"/><path d="M8 6.5l2 2-1.2 1.4c.7 1.4 1.8 2.5 3.2 3.2l1.4-1.2 2 2-1.3 1.6c-3.7-.4-7-3.7-7.4-7.4z" fill="#fff"/></svg>
        <span>(xx) xxxx-xxxx<br>(xx) xxxx-xxxx</span>
      </li>
      <li>
        <svg viewBox="0 0 22 22"><circle cx="11" cy="11" r="10" fill="var(--rose)"/><path d="M11 5a4 4 0 0 0-4 4c0 3 4 8 4 8s4-5 4-8a4 4 0 0 0-4-4z" fill="#fff"/><circle cx="11" cy="9" r="1.5" fill="var(--rose)"/></svg>
        <span>R. Seu Endereço<br>Cidade - Bairro<br>CEP: 00000-000</span>
      </li>
      <li>
        <svg viewBox="0 0 22 22"><circle cx="11" cy="11" r="10" fill="var(--rose)"/><rect x="6" y="7.5" width="10" height="7" fill="#fff"/><path d="M6 7.5l5 4 5-4" stroke="var(--rose)" fill="none"/></svg>
        <span>seuemail@exemplo.com</span>
      </li>
      <li>
        <svg viewBox="0 0 22 22"><circle cx="11" cy="11" r="10" fill="var(--rose)"/></svg>
        <span>/ginecologiaaurora</span>
      </li>
    </ul>

    <div class="figure" role="img" aria-label="Ilustração em traço de uma mulher envolta em tecido rosa"></div>
  </div>
</body>
</html>
```